3x-Kammerhof
Zielgruppe
3x-Kammerhof.de vermietet Lagercontainern an Privatkunden und Gewerbetriebende
Vermietung von Stellfächen für Wohnmobile/Boote etc
Das ganze auf einem Gewerbegelände in Köln (Brauweiler)
Aufgabenstellung
Erstellung eines 2-Seitigen DIN lang (10,5 x 21 cm) Flyers
Seite A: Vermietung von Lagercontainern
Seite B: Stellfächen für Wohnmobile/Boote
Wichtig: Die Sicherheit (Zutrittskontrolle, Videoüberwachung, Brandmeldeanlage)
Preise sollen auf Flyern erscheinen, diese wie auch die Textee möchte ich jedoch ändern können.
Alle Texte können auch von der Seite 3x-kammerhof.de übernommen werden
Das Logo (siehe stellhof_welt.ai) müsste noch bearbeitet werden .... also "stellhofwelt" raus und dafür "Lagerraum Container" rein
Gerne mit Symbolen arbeiten ..

```html
<!DOCTYPE html>
<html lang="de">
<head>
<meta charset="utf-8">
<title>3x-Kammerhof – Stellflächen für Wohnmobile / Boote</title>
<link rel="stylesheet" href="https://fonts.googleapis.com/css2?family=Barlow+Condensed:wght@500;600&family=Lato:wght@400;700;900&display=swap">
<style>
  :root {
    --navy: #0e2b4b;
    --red: #a8122a;
    --white: #ffffff;
    --mist: #e6e7ee;
    --ink: #0e2b4b;
    --note: #333a48;
  }
  * { margin: 0; padding: 0; box-sizing: border-box; }
  html, body { width: 1200px; height: 2400px; overflow: hidden; background: var(--white); }
  .flyer {
    position: relative; width: 1200px; height: 2400px; overflow: hidden;
    font-family: "Lato", sans-serif; color: var(--ink);
    background: linear-gradient(to bottom, var(--white) 0, var(--white) 900px, var(--mist) 1090px, var(--mist) 100%);
  }
  .masthead {
    position: absolute; left: 0; top: 0; width: 1200px; height: 335px;
    background: var(--navy);
    display: flex; align-items: center; justify-content: center;
  }
  .brand-name {
    font-family: "Lato", sans-serif; font-weight: 700;
    color: var(--white); font-size: 112px; line-height: 1; letter-spacing: 1px;
  }
  .promise-band {
    position: absolute; left: 0; top: 348px; width: 1200px; height: 144px;
    background: var(--red);
    display: flex; align-items: center; justify-content: center; gap: 68px;
  }
  .promise { display: flex; align-items: center; gap: 20px; color: var(--white); font-weight: 700; font-size: 70px; }
  .promise svg { width: 56px; height: 56px; }
  .offer-title {
    position: absolute; left: 0; top: 540px; width: 1200px; text-align: center;
    font-family: "Barlow Condensed", sans-serif; font-weight: 600;
    font-size: 64px; letter-spacing: 1.5px; color: var(--navy);
  }
  .vehicle-photo {
    position: absolute; left: 40px; top: 670px; width: 560px; height: 400px;
    border-radius: 40px 60px 20px 20px;
    background: linear-gradient(160deg, #f2f3f5 0%, #d9dce2 55%, #9ea4ae 100%);
  }
  .price-card {
    position: absolute; left: 622px; top: 665px; width: 528px; height: 383px;
    background: var(--navy); border-radius: 14px; color: var(--white);
    padding: 32px 40px 0 46px; box-shadow: inset 0 0 0 4px var(--navy), inset 0 0 0 7px rgba(255,255,255,0.25);
  }
  .price { font-weight: 700; font-size: 66px; line-height: 1; }
  .price small { font-size: 30px; font-weight: 700; margin-left: 10px; }
  .feature-list { list-style: none; margin-top: 32px; }
  .feature-list li { display: flex; align-items: center; gap: 12px; font-weight: 700; font-size: 29px; line-height: 44px; }
  .feature-list svg { width: 26px; height: 26px; flex: none; }
  .benefits {
    position: absolute; left: 45px; top: 1108px; width: 1110px; height: 1042px;
    background: var(--white); border: 6px solid var(--navy); border-radius: 18px;
  }
  .benefit { position: absolute; left: 0; width: 100%; }
  .benefit-label { position: absolute; left: 42px; top: -4px; font-size: 50px; font-weight: 700; color: var(--navy); }
  .benefit-icon { position: absolute; left: 74px; top: 100px; width: 170px; height: 140px; }
  .benefit-text { position: absolute; left: 352px; top: 4px; width: 740px; font-size: 35px; line-height: 58.5px; color: var(--navy); white-space: nowrap; }
  .footnote { position: absolute; left: 92px; top: 2177px; font-size: 17.5px; color: var(--note); }
  .contact-bar {
    position: absolute; left: 0; top: 2230px; width: 1200px; height: 170px;
    background: var(--navy); color: var(--white); font-weight: 700;
  }
  .contact-line { position: absolute; left: 0; width: 100%; display: flex; justify-content: center; align-items: center; gap: 30px; font-size: 33px; }
  .contact-line span { display: flex; align-items: center; gap: 10px; }
  .contact-line svg { width: 30px; height: 30px; }
</style>
</head>
<body>
<div class="flyer">
  <header class="masthead">
    <div class="brand-name">3x-Kammerhof</div>
  </header>

  <div class="promise-band">
    <div class="promise"><svg viewBox="0 0 24 24"><circle cx="12" cy="12" r="12" fill="#fff"/><path d="M6.5 12.5l3.7 3.6 7.3-7.6" fill="none" stroke="#a8122a" stroke-width="3" stroke-linecap="round" stroke-linejoin="round"/></svg>Günstig</div>
    <div class="promise"><svg viewBox="0 0 24 24"><circle cx="12" cy="12" r="12" fill="#fff"/><path d="M6.5 12.5l3.7 3.6 7.3-7.6" fill="none" stroke="#a8122a" stroke-width="3" stroke-linecap="round" stroke-linejoin="round"/></svg>Sicher</div>
    <div class="promise"><svg viewBox="0 0 24 24"><circle cx="12" cy="12" r="12" fill="#fff"/><path d="M6.5 12.5l3.7 3.6 7.3-7.6" fill="none" stroke="#a8122a" stroke-width="3" stroke-linecap="round" stroke-linejoin="round"/></svg>Lagern</div>
  </div>

  <h1 class="offer-title">STELLFLÄCHEN FÜR WOHNMOBILE / BOOTE</h1>

  <div class="vehicle-photo" role="img" aria-label="Foto eines weißen Wohnmobils"></div>

  <div class="price-card">
    <div class="price">148,- €<small>pro Monat*</small></div>
    <ul class="feature-list">
      <li><svg viewBox="0 0 24 24"><circle cx="12" cy="12" r="12" fill="#fff"/><path d="M6.5 12.5l3.7 3.6 7.3-7.6" fill="none" stroke="#0e2b4b" stroke-width="3.2" stroke-linecap="round" stroke-linejoin="round"/></svg>Durchgehend zugänglich</li>
      <li><svg viewBox="0 0 24 24"><circle cx="12" cy="12" r="12" fill="#fff"/><path d="M6.5 12.5l3.7 3.6 7.3-7.6" fill="none" stroke="#0e2b4b" stroke-width="3.2" stroke-linecap="round" stroke-linejoin="round"/></svg>14m² Lagerkapazität</li>
      <li><svg viewBox="0 0 24 24"><circle cx="12" cy="12" r="12" fill="#fff"/><path d="M6.5 12.5l3.7 3.6 7.3-7.6" fill="none" stroke="#0e2b4b" stroke-width="3.2" stroke-linecap="round" stroke-linejoin="round"/></svg>Versicherungsschutz möglich</li>
      <li><svg viewBox="0 0 24 24"><circle cx="12" cy="12" r="12" fill="#fff"/><path d="M6.5 12.5l3.7 3.6 7.3-7.6" fill="none" stroke="#0e2b4b" stroke-width="3.2" stroke-linecap="round" stroke-linejoin="round"/></svg>Zutrittskontrolle</li>
      <li><svg viewBox="0 0 24 24"><circle cx="12" cy="12" r="12" fill="#fff"/><path d="M6.5 12.5l3.7 3.6 7.3-7.6" fill="none" stroke="#0e2b4b" stroke-width="3.2" stroke-linecap="round" stroke-linejoin="round"/></svg>Videoüberwachung</li>
    </ul>
  </div>

  <section class="benefits">
    <div class="benefit" style="top:50px">
      <div class="benefit-label">Mehr Platz</div>
      <svg class="benefit-icon" viewBox="0 0 170 140"><rect x="60" y="10" width="58" height="58" rx="10" fill="#0e2b4b"/><rect x="26" y="76" width="58" height="58" rx="10" fill="#0e2b4b"/><rect x="94" y="76" width="58" height="58" rx="10" fill="#0e2b4b"/></svg>
      <p class="benefit-text">Verschaffen Sie sich mehr Platz! Ob privat<br>(Umzug, fehlende Garage, voller Keller)<br>oder gewerblich (zur Lagerung von Akten,<br>Gerätepark, Warenlager) – nutzen Sie Lager-<br>container zur Platzoptimierung.</p>
    </div>
    <div class="benefit" style="top:375px">
      <div class="benefit-label">Ebenerdig</div>
      <svg class="benefit-icon" viewBox="0 0 170 140"><rect x="58" y="40" width="60" height="60" rx="10" fill="#0e2b4b"/><rect x="14" y="116" width="148" height="10" fill="#0e2b4b"/></svg>
      <p class="benefit-text">Auf dem befestigten Gelände können Sie<br>auch mit großen Fahrzeugen direkt an die<br>Lagercontainer heranfahren und bequem<br>be- oder entladen, ohne große Wege gehen<br>zu müssen.</p>
    </div>
    <div class="benefit" style="top:700px">
      <div class="benefit-label">Rentabel</div>
      <svg class="benefit-icon" viewBox="0 0 170 140"><circle cx="88" cy="72" r="58" fill="#0e2b4b"/><circle cx="88" cy="72" r="47" fill="none" stroke="#fff" stroke-width="5"/><text x="88" y="92" text-anchor="middle" font-family="Lato, sans-serif" font-weight="900" font-size="58" fill="#fff">€</text></svg>
      <p class="benefit-text">Nutzen Sie den Platz in Ihrer Wohnung oder<br>Firma rentabler und lagern Sie die wichti-<br>gen, aber nicht täglich benötigten Dinge in<br>einen großen Lagerraum aus. Und das zu<br>fairen Preisen bei Top-Konditionen.</p>
    </div>
  </section>

  <p class="footnote">*Preis gilt pro Monat und Container für private Vermietung, bei gewerblicher Anmietung zzgl. 19% MwSt</p>

  <footer class="contact-bar">
    <div class="contact-line" style="top:36px">
      <span><svg viewBox="0 0 24 24"><path d="M12 2a7 7 0 0 0-7 7c0 5 7 13 7 13s7-8 7-13a7 7 0 0 0-7-7zm0 9.5A2.5 2.5 0 1 1 12 6.5a2.5 2.5 0 0 1 0 5z" fill="#fff"/></svg>Lindenhofstraße 27 im Gewerbegebiet Nordfeld</span>
    </div>
    <div class="contact-line" style="top:96px">
      <span><svg viewBox="0 0 24 24"><circle cx="12" cy="7" r="5" fill="#fff"/><path d="M3 22c0-6 4-9 9-9s9 3 9 9z" fill="#fff"/></svg>01234 5550199</span>
      <span><svg viewBox="0 0 24 24"><rect x="2" y="5" width="20" height="14" rx="2" fill="#fff"/><path d="M3 6l9 7 9-7" fill="none" stroke="#0e2b4b" stroke-width="2"/></svg>ft@3x-kammerhof.de</span>
      <span><svg viewBox="0 0 24 24"><circle cx="12" cy="12" r="10" fill="#fff"/><path d="M2 12h20M12 2c-4 5-4 15 0 20M12 2c4 5 4 15 0 20" fill="none" stroke="#0e2b4b" stroke-width="1.6"/></svg>3x-kammerhof.de</span>
    </div>
  </footer>
</div>
</body>
</html>
```